Brightwave Systems Business Cards
CHANGES::::::::
Dr. Helen T. Caldwell:
1) Cel Phone:
2) Title:
EMR Clinical Content Developer
2nd front of the card:
1) Name:
Dr. Gavin L. Thornby
EMR Implementation Specialist
3) Cel Phone:
4) Email:
gavin.thornby@brightwavesys-pr.example
I'm out...hope you find what you're looking for :)
PLEASE NOTE:
Addres:
Linden Court Plaza #3, Suite 518
San Juan, PR 00947
New phone #:
Fax #:

```html
<!DOCTYPE html>
<html lang="en">
<head>
<meta charset="utf-8">
<title>Brightwave Systems Stationery</title>
<link href="https://fonts.googleapis.com/css2?family=Nunito:wght@400;700;800&display=swap" rel="stylesheet">
<style>
:root{
  --bg:#4a3b31;
  --orange:#f7941d;
  --dark:#2b2b2d;
  --dark-soft:#3a3a3c;
  --paper:#ffffff;
  --ink:#444;
  --muted:#8a8a8a;
  --faint:#fbe3c8;
}
*{box-sizing:border-box;margin:0;padding:0}
html,body{width:1200px;height:701px;overflow:hidden}
body{background:var(--bg);font-family:"Nunito",sans-serif;color:var(--ink);position:relative}
.item{position:absolute;overflow:hidden;box-shadow:0 2px 6px rgba(0,0,0,.35)}
.brand{font-family:"Nunito",sans-serif;font-weight:800;color:var(--orange);display:flex;align-items:center;gap:5px;white-space:nowrap;line-height:1}
.brand .dot{width:12px;height:12px;border-radius:50%;background:var(--orange);flex:none}
.card .brand{font-size:8px;gap:4px}
.card .brand .dot{width:9px;height:9px}
.faint-circle{position:absolute;border-radius:50%;border:14px solid var(--faint)}
/* business cards */
.card{width:132px;height:80px;background:var(--paper)}
.card.dark{background:var(--dark)}
.card.orange{background:var(--orange)}
.card .band{position:absolute;left:0;right:0;bottom:0;height:10px;background:var(--dark)}
.card .band.or{background:var(--orange)}
.person{position:absolute;left:10px;top:12px;font-size:7px;line-height:1.35}
.person .name{font-weight:800;font-size:7.5px}
.person .title{color:var(--muted);font-size:5px}
.contact{position:absolute;left:10px;bottom:15px;font-size:5px;line-height:1.4;color:var(--muted);white-space:nowrap}
.dark .person .name{color:#fff}
.dark .contact{color:#bbb}
/* envelopes */
.envelope{width:210px;height:96px;background:var(--paper)}
.envelope.dark{background:var(--dark)}
.envelope.orange{background:var(--orange)}
.envelope svg{position:absolute;inset:0}
/* slips */
.slip{background:var(--paper);width:252px}
.slip .footer{position:absolute;left:0;right:0;bottom:0;height:8px;background:var(--dark)}
.slip .addr{position:absolute;left:14px;font-size:5.5px;line-height:1.4;color:var(--muted)}
.window{position:absolute;right:18px;bottom:22px;width:80px;height:24px;border:1px solid #ccc;background:#f3f3f3}
.folder{width:150px;height:130px;background:var(--dark)}
.folder .flap{position:absolute;left:0;right:0;top:0;height:26px;background:var(--dark-soft)}
/* letterhead */
.letter{width:288px;height:408px;background:var(--paper)}
.letter .top{position:absolute;left:0;right:0;top:0;height:6px;background:var(--dark)}
.letter .web{position:absolute;right:14px;top:16px;font-size:5.5px;color:var(--muted)}
.letter .body{position:absolute;left:22px;right:26px;top:62px;font-size:5.3px;line-height:1.55;color:var(--ink)}
.letter .body p{margin-bottom:7px}
.letter .foot{position:absolute;left:0;right:0;bottom:0;height:22px;background:var(--dark);color:#ccc;font-size:5px;display:flex;align-items:center;justify-content:center;gap:12px}
.letter .foot span.or{color:var(--orange)}
</style>
</head>
<body>

<!-- business cards -->
<div class="item card" style="left:12px;top:50px">
  <div class="brand" style="position:absolute;left:14px;top:32px"><span class="dot"></span>Brightwave Systems</div>
  <div class="band"></div>
</div>
<div class="item card" style="left:152px;top:50px">
  <div class="faint-circle" style="width:90px;height:90px;right:-20px;top:-5px"></div>
  <div class="band or"></div>
</div>

<div class="item card dark" style="left:12px;top:140px">
  <div class="person"><div class="name">Dr. Helen T. Caldwell</div><div class="title">EMR Clinical Content Developer</div></div>
  <div class="contact">Cel: 787.555.0142<br>helen@brightwavesys-pr.example</div>
  <div class="band or"></div>
</div>
<div class="item card orange" style="left:152px;top:140px">
  <div class="faint-circle" style="width:70px;height:70px;left:8px;top:5px;border-color:var(--dark);border-width:12px"></div>
  <div class="brand" style="position:absolute;left:80px;top:62px;font-size:7px;color:var(--dark)">Brightwave</div>
</div>

<div class="item card" style="left:12px;top:230px">
  <div class="person"><div class="name">Dr. Gavin L. Thornby</div><div class="title">EMR Implementation Specialist</div></div>
  <div class="contact">Cel: 787.555.0188<br>gavin.thornby@brightwavesys-pr.example</div>
  <div class="band or"></div>
</div>
<div class="item card dark" style="left:152px;top:230px">
  <div class="brand" style="position:absolute;left:14px;top:36px"><span class="dot"></span>Brightwave Systems</div>
</div>

<!-- compliment envelopes -->
<div class="item slip" style="left:12px;top:326px;height:108px">
  <div class="brand" style="position:absolute;left:14px;top:14px;font-size:11px"><span class="dot"></span>Brightwave Systems</div>
  <div class="addr" style="top:74px">Linden Court Plaza #3, Suite 518<br>San Juan, PR 00947</div>
  <div class="footer"></div>
</div>
<div class="item slip" style="left:12px;top:452px;height:140px">
  <div style="position:absolute;left:0;right:0;top:0;height:6px;background:var(--orange)"></div>
  <div class="brand" style="position:absolute;left:14px;top:16px;font-size:10px"><span class="dot"></span>Brightwave Systems</div>
  <div class="addr" style="top:34px">Linden Court Plaza #3, Suite 518<br>San Juan, PR 00947</div>
  <div class="window"></div>
  <div class="footer"></div>
</div>

<div class="item folder" style="left:286px;top:326px">
  <div class="flap"></div>
  <div class="faint-circle" style="width:70px;height:70px;left:20px;top:40px;border-color:var(--orange);border-width:12px"></div>
  <div class="brand" style="position:absolute;left:90px;top:108px;font-size:7px">Brightwave</div>
</div>

<!-- envelopes -->
<div class="item envelope dark" style="left:528px;top:48px">
  <svg viewBox="0 0 210 96" aria-hidden="true"><path d="M0 0 L105 46 L210 0" fill="none" stroke="#444" stroke-width="1.5"/></svg>
  <div class="brand" style="position:absolute;left:10px;top:72px;font-size:8px"><span class="dot" style="width:9px;height:9px"></span>Brightwave Systems</div>
</div>
<div class="item envelope" style="left:748px;top:56px">
  <svg viewBox="0 0 210 96" aria-hidden="true"><path d="M0 0 L105 46 L210 0" fill="none" stroke="#ddd" stroke-width="1.5"/></svg>
  <div class="brand" style="position:absolute;left:10px;top:72px;font-size:8px"><span class="dot" style="width:9px;height:9px"></span>Brightwave Systems</div>
</div>
<div class="item envelope orange" style="left:968px;top:64px">
  <svg viewBox="0 0 210 96" aria-hidden="true"><path d="M0 0 L105 46 L210 0" fill="none" stroke="#fbb15e" stroke-width="1.5"/></svg>
  <div class="faint-circle" style="width:46px;height:46px;left:82px;top:18px;border-color:#fff;border-width:8px"></div>
</div>

<!-- letterheads -->
<div class="item letter" style="left:540px;top:200px">
  <div class="top"></div>
  <div class="brand" style="position:absolute;left:22px;top:18px;font-size:11px"><span class="dot"></span>Brightwave Systems</div>
  <div class="web">brightwavesys-pr.example</div>
  <div class="body">
    <p>May 1, 2024</p>
    <p>Recipient Name<br>Company Address<br>San Juan, PR 00900</p>
    <p>Dear Mr. Recipient,</p>
    <p>Thank you for your interest in our services. Our team builds and supports electronic medical record systems for clinics across the island, with care and attention to every workflow.</p>
    <p>We would welcome the chance to meet with your staff and show how a smooth rollout can save time for doctors and patients alike.</p>
    <p>Please contact our office at your convenience to arrange a visit.</p>
    <p>Sincerely,<br><br>Dr. Helen T. Caldwell</p>
  </div>
  <div class="foot"><span>Linden Court Plaza #3, Suite 518, San Juan, PR 00947</span><span class="or">T 787.555.0142</span></div>
</div>

<div class="item letter" style="left:856px;top:200px">
  <div class="top"></div>
  <div class="faint-circle" style="width:150px;height:150px;right:-10px;bottom:50px;border-width:22px"></div>
  <div class="brand" style="position:absolute;left:22px;top:18px;font-size:11px"><span class="dot"></span>Brightwave Systems</div>
  <div class="web">brightwavesys-pr.example</div>
  <div class="body">
    <p>May 1, 2024</p>
    <p>Recipient Name<br>Company Address<br>San Juan, PR 00900</p>
    <p>Dear Ms. Recipient,</p>
    <p>It was a pleasure to speak with you last week. As promised, we are sending an outline of our training plan for your clinical and front desk teams during the system launch.</p>
    <p>Our specialists will stay on site through the first weeks to answer questions and adjust settings as your needs grow.</p>
    <p>We look forward to working with you soon.</p>
    <p>Kind regards,<br><br>Dr. Gavin L. Thornby</p>
  </div>
  <div class="foot"><span>Linden Court Plaza #3, Suite 518, San Juan, PR 00947</span><span class="or">T 787.555.0142</span></div>
</div>

</body>
</html>
```